Business card Zottelgarten

Business card is for a self-employed dog trainer with own dog school. Name and logo of the dog school are available. Color specifications as well. The design should be classy and minimalist, but also modern. An already existing idea would be: Front: Only the logo Back: Contact data

Font styles to use
Serif
Sans Serif
Other font styles liked:
• Trajan Pro

Colors
f78f20

Requirements
Must have
• Name: Margit Wendler-Rasch Title: Dipl. Dog Trainer Contain my logo Follow my font and color preferences (see files)

```html
<!DOCTYPE html>
<html lang="de">
<head>
<meta charset="utf-8">
<title>Zottelgarten – Visitenkarte</title>
<link rel="stylesheet" href="https://fonts.googleapis.com/css2?family=Cinzel:wght@400;500&family=Lato:wght@400;700&display=swap">
<style>
  :root {
    --brand-orange: #f78f20;
    --card-white: #f2f2f2;
    --ink-dark: #3a3a3a;
    --backdrop: #2e2e2e;
    --white: #ffffff;
  }
  * { box-sizing: border-box; margin: 0; padding: 0; }
  html, body {
    width: 1200px; height: 900px; overflow: hidden;
    background: var(--backdrop);
  }
  .stage { position: relative; width: 1200px; height: 900px; }
  .card {
    position: absolute;
    width: 560px; height: 320px;
    border-radius: 22px;
    overflow: hidden;
  }
  .card--front { left: 70px; top: 90px; background: var(--brand-orange); }
  .card--back { left: 570px; top: 490px; background: var(--card-white); }

  .wordmark { display: flex; flex-direction: column; align-items: center; }
  .wordmark__circle { border-radius: 50%; }
  .wordmark__name {
    font-family: "Cinzel", serif; font-weight: 400;
    letter-spacing: 1px; line-height: 1;
  }
  .wordmark__url {
    font-family: "Cinzel", serif; font-weight: 400;
    letter-spacing: 6px; line-height: 1;
  }

  .card--front .wordmark { position: absolute; left: 0; right: 0; top: 48px; }
  .card--front .wordmark__circle {
    width: 150px; height: 150px; background: var(--white);
    box-shadow: 0 0 0 3px var(--brand-orange), 0 0 0 5px var(--white);
  }
  .card--front .wordmark__name { color: var(--white); font-size: 44px; margin-top: 14px; }
  .card--front .wordmark__url { color: var(--white); font-size: 11px; margin-top: 6px; }

  .card--back .wordmark { position: absolute; left: 20px; width: 250px; top: 92px; }
  .card--back .wordmark__circle {
    width: 100px; height: 100px; background: var(--brand-orange);
    box-shadow: 0 0 0 2px var(--card-white), 0 0 0 3px var(--brand-orange);
  }
  .card--back .wordmark__name { color: var(--brand-orange); font-size: 29px; margin-top: 10px; }
  .card--back .wordmark__url { color: var(--brand-orange); font-size: 8px; margin-top: 5px; letter-spacing: 4.5px; }

  .divider {
    position: absolute; left: 292px; top: 58px;
    width: 2px; height: 210px; background: var(--brand-orange);
  }
  .contact { position: absolute; left: 318px; top: 66px; font-family: "Lato", sans-serif; }
  .contact__name { color: var(--ink-dark); font-size: 24px; font-weight: 400; }
  .contact__title { color: var(--brand-orange); font-size: 13px; margin-top: 2px; }
  .contact__list { list-style: none; margin-top: 22px; }
  .contact__item {
    display: flex; align-items: center; gap: 10px;
    color: var(--ink-dark); font-size: 14px; margin-bottom: 11px;
  }
  .contact__item--social { color: var(--brand-orange); margin-top: 8px; }
  .contact__icon { width: 16px; height: 16px; flex: none; }
  .contact__badge { width: 14px; height: 14px; background: var(--brand-orange); border-radius: 2px; flex: none; }
</style>
</head>
<body>
<main class="stage">
  <section class="card card--front" aria-label="Vorderseite">
    <div class="wordmark">
      <div class="wordmark__circle"></div>
      <p class="wordmark__name">ZOTTELGARTEN</p>
      <p class="wordmark__url">WWW.ZOTTELGARTEN.CH</p>
    </div>
  </section>

  <section class="card card--back" aria-label="Rückseite">
    <div class="wordmark">
      <div class="wordmark__circle"></div>
      <p class="wordmark__name">ZOTTELGARTEN</p>
      <p class="wordmark__url">WWW.ZOTTELGARTEN.CH</p>
    </div>
    <div class="divider"></div>
    <div class="contact">
      <h1 class="contact__name">Margit Wendler-Rasch</h1>
      <p class="contact__title">Dipl. Hundetrainerin</p>
      <ul class="contact__list">
        <li class="contact__item">
          <svg class="contact__icon" viewBox="0 0 16 16" aria-hidden="true">
            <path d="M1 5 Q8 1 15 5 L13 7 L11 6 L11 5 Q8 4 5 5 L5 6 L3 7 Z" fill="#f78f20"/>
            <path d="M4 8 L12 8 L14 14 L2 14 Z" fill="#f78f20"/>
            <circle cx="8" cy="11" r="1.6" fill="#f2f2f2"/>
          </svg>
          <span>000 000 0000</span>
        </li>
        <li class="contact__item">
          <svg class="contact__icon" viewBox="0 0 16 16" aria-hidden="true">
            <rect x="1" y="3" width="14" height="10" fill="#f78f20"/>
            <path d="M1 3 L8 9 L15 3" fill="none" stroke="#f2f2f2" stroke-width="1.3"/>
          </svg>
          <span>youremail@xyz.com</span>
        </li>
        <li class="contact__item contact__item--social">
          <span class="contact__badge"></span>
          <span>/zottelgarten</span>
        </li>
      </ul>
    </div>
  </section>
</main>
</body>
</html>
```